WP website design for Dorrance

We need a wordpress design that will incorporate a professional color scheme with company logo in a clean layout. The design needs to consider that this will be developed on a responsive theme. Colors are will be the green of the logo and any others that will creatively highlight it.

Industry/Entity Type

It Company

Font styles to use
Sans Serif

Requirements
Must have
• Navigation: 1) Home 2) Auctions 3) Auction Services 4) Sellers 5) KT Dorrance Livestock 6) About Us 7) Contact Us
Site will have slideshow element, image attached.
Widgets will be: 1)Email Signup form 2) Featured Auctions widget 3) Social Media (FB, plain square, RSS) 4) News & Events blog
Footer will have smaller company logo, association logos (attached) and contact info (below)
▪ K.T. Dorrance Inc. / Auctioneers
▪ 4715 NC Hwy 91
▪ Belmora, NC 27640
▪ Office: (252) 555-0187
▪ Cell: (252) 555-0163
▪ email: ktdorrance@ktdorrance-example.com
Nice to have
• Site will have drop-down menus - please indicate the styling, for instance the dropdown menus

```html
<!DOCTYPE html>
<html lang="en">
<head>
<meta charset="utf-8">
<title>K.T. Dorrance Inc. / Auctioneers</title>
<link href="https://fonts.googleapis.com/css2?family=Open+Sans:wght@400;600;700&family=Parisienne&display=swap" rel="stylesheet">
<style>
:root{
  --green:#2f7d12;
  --green-dark:#256a0c;
  --green-light:#3e9a1a;
  --green-text:#2a7a10;
  --page:#f1f1f1;
  --white:#ffffff;
  --ink:#222222;
  --muted:#555555;
  --orange:#d06a12;
  --red:#c0282e;
  --link:#3a4fd0;
  --card:#f7f7f7;
}
*{box-sizing:border-box;margin:0;padding:0}
html,body{width:839px;height:1200px;overflow:hidden}
body{background:var(--page);font-family:"Open Sans",Arial,sans-serif;color:var(--ink);position:relative;font-size:9px}
.abs{position:absolute}
.script{font-family:"Parisienne",cursive;color:var(--green-text);font-weight:400}

/* header */
.header-bg{left:0;top:0;width:839px;height:92px;background:linear-gradient(90deg,#f7f7f7 0%,#f2eef6 70%,#ebe3f1 100%)}
.social{right:95px;top:3px;display:flex;gap:6px}
.social span{width:25px;height:25px;border-radius:3px;display:block}
.social .s1{background:#2f4f8f}.social .s2{background:#c4282a}.social .s3{background:#e86a1c}
.contact-top{right:95px;top:42px;text-align:right;color:var(--green-text);font-size:15px;line-height:22px;font-weight:600}
.contact-top .ico{display:inline-block;width:15px;height:10px;background:var(--green-light);border-radius:2px;margin-right:5px;vertical-align:middle}

.navbar{left:0;top:92px;width:839px;height:24px;background:var(--green)}
.nav{left:258px;top:92px;display:flex;height:24px}
.nav a{color:var(--white);text-decoration:none;font-size:10px;line-height:24px;padding:0 12px}
.nav a.active{background:#e9efe4;color:var(--green-text)}
.dropdown{left:306px;top:128px;width:105px;background:rgba(62,140,30,.88);border:1px solid #7fb35f;border-radius:2px}
.dropdown a{display:block;color:#fff;font-size:8.5px;line-height:21px;padding-left:9px;border-bottom:1px solid rgba(255,255,255,.25);text-decoration:none}

.logo{left:95px;top:0;width:150px;height:128px;background:var(--white);border:1px solid #c9d9bf;clip-path:polygon(0 0,100% 0,100% 88%,50% 100%,0 88%);display:flex;flex-direction:column;align-items:center;justify-content:center;gap:6px}
.logo .mark{width:22px;height:22px;border-radius:50%;background:var(--green)}
.logo .name{color:var(--green-text);font-weight:700;font-size:13px;text-align:center;line-height:15px}

/* slider */
.slide{left:95px;top:116px;width:472px;height:249px;background:linear-gradient(180deg,#d9e6f2 0%,#c7a36a 35%,#8a7a4e 48%,#6d6a55 70%,#8d7a56 100%)}
.dots{left:303px;top:350px;display:flex;gap:3px}
.dots span{width:11px;height:11px;border:1px solid #999;background:#fff}
.dots span.on{background:var(--red)}

.featured{left:567px;top:116px;width:177px;height:249px;background:#ececec;border:1px solid #d5d5d5}
.featured .head{height:33px;background:var(--green);color:#fff;font-family:"Parisienne",cursive;font-size:22px;text-align:center;line-height:33px}
.featured .photo{height:82px;background:linear-gradient(180deg,#c8e3ef,#b5d59a)}
.featured .body{padding:3px 10px;font-size:8px;line-height:11px;color:var(--muted)}
.featured .title{color:var(--green-text);font-size:13px;line-height:16px}
.featured .label{color:var(--green-text);font-weight:700;margin-top:8px}
.fdots{left:638px;top:352px;display:flex;gap:2px}
.fdots span{width:7px;height:7px;background:var(--green-light)}.fdots span.on{background:var(--red)}

/* signup */
.signup{left:95px;top:365px;width:649px;height:55px;background:var(--green)}
.signup p{position:absolute;left:17px;top:11px;color:#fff;font-size:11.5px;line-height:15px}
.signup .field{position:absolute;top:11px;height:29px;background:#fff;color:#aaa;font-size:8.5px;line-height:29px;padding-left:9px}
.signup .btn{position:absolute;left:542px;top:11px;width:95px;height:29px;background:var(--green-light);border:1px solid #8bc96a;color:#fff;font-size:12px;text-align:center;line-height:27px}

/* content */
.main{left:95px;top:420px;width:649px;height:430px;background:#fbfbfb}
.welcome{left:108px;top:434px;font-size:26px}
.intro{left:108px;top:469px;width:624px;font-size:8.5px;line-height:11.5px;color:var(--ink)}
.sec-title{left:108px;top:531px;font-size:21px}
.sec-line{left:252px;top:548px;width:444px;height:2px;background:var(--green)}
.arrows{left:698px;top:535px;display:flex;gap:3px}
.arrows span{width:14px;height:14px;background:var(--green);color:#fff;font-size:9px;text-align:center;line-height:14px}

.card{top:558px;width:224px;height:270px;background:var(--card);border:1px solid #dedede}
.card .head{height:24px;background:var(--green);color:#fff;font-weight:600;font-size:11.5px;line-height:24px;padding-left:11px}
.card .thumb{position:absolute;left:12px;top:35px;width:96px;height:77px}
.card .links{position:absolute;left:118px;top:52px;font-size:8.5px;line-height:21px;color:var(--link)}
.card .links i{display:inline-block;width:11px;height:9px;background:#e6b52e;margin-right:4px;vertical-align:middle}
.card .links i.d{background:#6aa7e0}
.card h3{position:absolute;left:11px;top:118px;font-size:9.5px;font-weight:600}
.card .txt{position:absolute;left:11px;top:134px;width:200px;font-size:8.3px;line-height:11.5px}
.card .info{position:absolute;left:11px;top:174px;width:190px;height:88px;border:1px solid #d7d7d7;background:#f1f1f1;padding:6px;font-size:8.2px;line-height:13px}
.card .info b{color:#5a3b00}
.card .info .bid{color:var(--link)}
.card .info .bid i{display:inline-block;width:16px;height:10px;background:#9bb7d4;margin-right:5px;vertical-align:middle}
.card .info .loc{padding-left:45px;text-indent:-45px}

.lower{left:95px;top:849px;width:649px;height:157px;background:#f7f7f7;border:1px solid #dcdcdc}
.testi-title{left:123px;top:852px;color:var(--green-text);font-weight:700;font-size:14px}
.testi{left:125px;top:885px;width:175px;font-size:8.5px;line-height:12px;color:var(--muted)}
.testi .q{color:#ccc;font-size:22px;font-family:Georgia,serif}
.testi-name{left:215px;top:958px;color:var(--red);font-size:11px;text-align:right}
.testi-place{left:211px;top:972px;color:var(--muted);font-size:11px}
.tdots{left:108px;top:992px;display:flex;gap:2px}
.tdots span{width:8px;height:8px;background:#111}.tdots span.on{background:var(--red)}
.divider{left:322px;top:860px;width:4px;height:130px;background:linear-gradient(90deg,#ddd,transparent)}
.news-title{left:371px;top:857px;color:var(--green-text);font-weight:700;font-size:14px}
.news-line{left:481px;top:867px;width:249px;height:5px;background:var(--green)}
.news{top:884px;width:178px}
.news h4{color:var(--green-text);font-weight:400;font-size:11px;margin-bottom:6px;white-space:nowrap}
.news p{font-size:8px;line-height:10.5px;color:var(--muted)}
.news .meta{position:absolute;top:86px;width:178px;font-size:8px;color:var(--orange);display:flex;justify-content:space-between}
.news-sep{left:548px;top:908px;width:1px;height:65px;background:#d5d5d5}
.viewall{left:372px;top:990px;font-size:8.5px;color:var(--red);font-weight:600}

/* footer */
.footer{left:0;top:1026px;width:839px;height:151px;background:var(--green)}
.f-head{top:1038px;color:#cfe8bf;font-size:10px}
.f-menu{left:94px;top:1056px;color:#fff;font-size:9.5px;line-height:14.5px;list-style:none}
.f-sep{top:1062px;width:1px;height:84px;background:#5fa640}
.badge{background:#e9e9e9;border:2px solid #fff}
.f-logo{left:504px;top:1060px;width:81px;height:69px;background:#fff;clip-path:polygon(0 0,100% 0,100% 88%,50% 100%,0 88%);display:flex;flex-direction:column;align-items:center;justify-content:center;gap:3px}
.f-logo .mark{width:12px;height:12px;border-radius:50%;background:var(--green)}
.f-logo .name{color:var(--green-text);font-weight:700;font-size:7.5px;text-align:center;line-height:9px}
.f-contact{left:595px;color:#fff;font-size:9px;line-height:12px}
.f-contact svg{position:absolute;left:-2px;top:1px}
.f-contact span{padding-left:13px;display:block}
.copy{left:0;top:1177px;width:839px;height:23px;background:var(--green-dark);color:#e6f0de;font-size:8px;text-align:center;line-height:23px}
</style>
</head>
<body>
<div class="abs header-bg"></div>
<div class="abs social" aria-label="Social media links">
  <span class="s1" title="Social page"></span><span class="s2" title="Video channel"></span><span class="s3" title="News feed"></span>
</div>
<div class="abs contact-top">
  <div>(252) 555-0187</div>
  <div><span class="ico"></span>ktdorrance@ktdorrance-example.com</div>
</div>

<div class="abs navbar"></div>
<nav class="abs nav">
  <a href="#">Home</a><a href="#" class="active">Auctions</a><a href="#">Auction Services</a><a href="#">Sellers</a><a href="#">KT Dorrance Livestock</a><a href="#">About Us</a><a href="#">Contact Us</a>
</nav>

<div class="abs slide" role="img" aria-label="Slideshow photo of a calm pond reflecting autumn trees and a grassy bank"></div>
<div class="abs dots"><span class="on"></span><span></span><span></span><span></span></div>

<div class="abs dropdown">
  <a href="#">-- Current Auctions</a><a href="#">-- Past Auctions</a><a href="#" style="border:0">-- Featured Auctions</a>
</div>

<div class="abs logo">
  <span class="mark"></span>
  <span class="name">K.T. Dorrance Inc.<br>/ Auctioneers</span>
</div>

<aside class="abs featured">
  <div class="head">Featured Auctions</div>
  <div class="photo" role="img" aria-label="Photo of horses running in a meadow"></div>
  <div class="body">
    <div class="title">Auction Title</div>
    Lorem Ipsum. Proin gravida nibh vel velit auctor aliquet. Aenean sollicitudin, lorem quis bibendum auctor, nisi elit consequat ipsum, nec sagittis sem nibh id elit..
    <div class="label">Begins:</div>Monday,29-Sep-2014 at 8:00 AM CDT
    <div class="label" style="margin-top:4px">End:</div>Monday,06-Oct-2014 at 8:00 AM CDT
  </div>
</aside>
<div class="abs fdots"><span></span><span class="on"></span><span></span><span></span></div>

<form class="abs signup">
  <p>Please fillup your name and email to<br>receive updates on upcoming auctions</p>
  <div class="field" style="left:224px;width:156px">Enter your name..</div>
  <div class="field" style="left:384px;width:155px">Enter your email address..</div>
  <div class="btn">Send</div>
</form>

<div class="abs main"></div>
<h1 class="abs script welcome">Welcome to K.T. Dorrance Inc. / Auctioneers</h1>
<p class="abs intro">Lorem Ipsum. Proin gravida nibh vel velit auctor aliquet. Aenean sollicitudin, lorem quis bibendum auctor, nisi elit consequat ipsum, nec sagittis sem nibh id elit. Duis sed odio sit amet nibh vulputate cursus a sit amet mauris. Morbi accumsan ipsum velit. Nam nec tellus a odio tincidunt auctor a ornare odio. Sed non &nbsp;mauris vitae erat consequat auctor eu in elit. Class aptent taciti sociosqu ad litora torquent per conubia nostra, per inceptos himenaeos. Mauris in erat justo.</p>

<h2 class="abs script sec-title">Current Auctions</h2>
<div class="abs sec-line"></div>
<div class="abs arrows"><span>&#9664;</span><span>&#9654;</span></div>

<article class="abs card" style="left:108px">
  <div class="head">Auctions Title here</div>
  <div class="thumb" role="img" aria-label="Photo of a country house with porch and garden" style="background:linear-gradient(160deg,#9cc46a,#d8d0b8 55%,#5f8a3a)"></div>
  <div class="links"><div><i class="d"></i>Details</div><div><i></i>Photo Galleries</div></div>
  <h3>LOREM IPSUM PROIN GRAVIDA NIBH</h3>
  <p class="txt">Lorem Ipsum. Proin gravida nibh vel velit auctor aliquet. Aenean sollicitudin, lorem quis bibendum auctor, nisi elit consequat</p>
  <div class="info"><b>Begins:</b> Monday, 29-Sep-2014 at 4:00 PM<br>LIVE ON-SITE AUCTION<br><span class="bid"><i></i>Click Here to Bid Online Now!</span><div class="loc"><b>Location:</b> Lorem Ipsum proin gravida nibh vel nibhvelit Ipsum.</div></div>
</article>
<article class="abs card" style="left:317px">
  <div class="head">Auctions Title here</div>
  <div class="thumb" role="img" aria-label="Photo of a brick house with lawn" style="background:linear-gradient(170deg,#a9cbe8,#8c4a34 45%,#6c9a3e)"></div>
  <div class="links"><div><i class="d"></i>Details</div><div><i></i>Photo Galleries</div></div>
  <h3>LOREM IPSUM PROIN GRAVIDA NIBH</h3>
  <p class="txt">Lorem Ipsum. Proin gravida nibh vel velit auctor aliquet. Aenean sollicitudin, lorem quis bibendum auctor, nisi elit consequat</p>
  <div class="info"><b>Begins:</b> Monday, 29-Sep-2014 at 4:00 PM<br>LIVE ON-SITE AUCTION<br><span class="bid"><i></i>Click Here to Bid Online Now!</span><div class="loc"><b>Location:</b> Lorem Ipsum proin gravida nibh vel nibhvelit Ipsum.</div></div>
</article>
<article class="abs card" style="left:525px">
  <div class="head">Auctions Title here</div>
  <div class="thumb" role="img" aria-label="Photo of a white vintage car" style="background:linear-gradient(180deg,#7a6a5a,#d9d9d9 55%,#6a5a4a)"></div>
  <div class="links"><div><i class="d"></i>Details</div><div><i></i>Photo Galleries</div></div>
  <h3>LOREM IPSUM PROIN GRAVIDA NIBH</h3>
  <p class="txt">Lorem Ipsum. Proin gravida nibh vel velit auctor aliquet. Aenean sollicitudin, lorem quis bibendum auctor, nisi elit consequat</p>
  <div class="info"><b>Begins:</b> Monday, 29-Sep-2014 at 4:00 PM<br>LIVE ON-SITE AUCTION<br><span class="bid"><i></i>Click Here to Bid Online Now!</span><div class="loc"><b>Location:</b> Lorem Ipsum proin gravida nibh vel nibhvelit Ipsum.</div></div>
</article>

<section class="abs lower"></section>
<h2 class="abs testi-title">TESTIMONIALS</h2>
<p class="abs testi"><span class="q">&ldquo;</span>Lorem Ipsum. Proin gravida nibh vel velit auctor aliquet. Aenean sol icit udin, lorem quis bibendumoilp auctor, nisi elit consequat ipsum, nec sagitt sem nibh id elit.<span class="q">&rdquo;</span></p>
<div class="abs testi-name">- Lena R</div>
<div class="abs testi-place">Belmora</div>
<div class="abs tdots"><span></span><span class="on"></span><span></span><span></span></div>
<div class="abs divider"></div>

<h2 class="abs news-title">NEWS &amp; EVENTS</h2>
<div class="abs news-line"></div>
<div class="abs news" style="left:372px">
  <h4>Lorem Ipsum proin gravida nibh ve</h4>
  <p>Lorem Ipsum proin gravida nibh vel veli auctor &nbsp;Ipsum proin gravida nibh vel veli gravida nibh vel gravida nibh Lorem Ipsum proin gravida ...</p>
  <div class="meta"><span>29/09/2014</span><span>Learn more &rarr;</span></div>
</div>
<div class="abs news-sep"></div>
<div class="abs news" style="left:565px">
  <h4>Lorem Ipsum proin gravida nibh ve</h4>
  <p>Lorem Ipsum proin gravida nibh vel veli auctor &nbsp;Ipsum proin gravida nibh vel veli gravida nibh vel gravida nibh Lorem Ipsum proin gravida ...</p>
  <div class="meta"><span>29/09/2014</span><span>Learn more &rarr;</span></div>
</div>
<div class="abs viewall">View All &rsaquo;</div>

<footer class="abs footer"></footer>
<div class="abs f-head" style="left:94px">MENU</div>
<ul class="abs f-menu">
  <li>Home</li><li>Auctions</li><li>Auction Services</li><li>Sellers</li><li>KT Dorrance Livestock</li><li>About Us</li><li>Contact Us</li>
</ul>
<div class="abs f-sep" style="left:217px"></div>
<div class="abs f-head" style="left:314px">ASSOCIATION</div>
<div class="abs badge" style="left:293px;top:1061px;width:85px;height:28px;border-radius:4px" role="img" aria-label="Association member badge"></div>
<div class="abs badge" style="left:285px;top:1104px;width:56px;height:40px;border-radius:6px" role="img" aria-label="Partner badge"></div>
<div class="abs badge" style="left:349px;top:1104px;width:42px;height:42px;border-radius:50%" role="img" aria-label="Partner badge"></div>
<div class="abs f-sep" style="left:457px"></div>
<div class="abs f-head" style="left:506px">CONTACT INFO</div>
<div class="abs f-logo"><span class="mark"></span><span class="name">K.T. Dorrance Inc.<br>/ Auctioneers</span></div>
<div class="abs f-contact" style="top:1058px">
  <svg width="9" height="12" viewBox="0 0 9 12"><path d="M4.5 0a4.5 4.5 0 0 0-4.5 4.5C0 8 4.5 12 4.5 12S9 8 9 4.5A4.5 4.5 0 0 0 4.5 0zm0 6.5a2 2 0 1 1 0-4 2 2 0 0 1 0 4z" fill="#fff"/></svg>
  <span>K.T. Dorrance Inc. / Auctioneers<br>4715 NC Hwy 91<br>Belmora, NC 27640</span>
</div>
<div class="abs f-contact" style="top:1113px">
  <svg width="10" height="10" viewBox="0 0 10 10"><path d="M1 3c0-1 1-2 4-2s4 1 4 2H7V2H3v1zM2 4h6l1 5H1z" fill="#fff"/></svg>
  <span>(252) 555-0187</span>
</div>
<div class="abs f-contact" style="top:1134px">
  <svg width="8" height="11" viewBox="0 0 8 11"><rect x="0.5" y="0.5" width="7" height="10" rx="1" fill="none" stroke="#fff"/></svg>
  <span>(252) 555-0163</span>
</div>
<div class="abs f-contact" style="top:1154px">
  <svg width="10" height="9" viewBox="0 0 10 9"><path d="M0 3l5-3 5 3v6H0z" fill="#fff"/></svg>
  <span>email: ktdorrance@ktdorrance-example.com</span>
</div>
<div class="abs copy">Copyright &copy; 2 2014 K.T. Dorrance Inc. / Auctioneers | All Rights Reserved.</div>
</body>
</html>
```